Letterhead design for business

Looking for an attractive and professional letterhead that uses the logo that is attached below.

Target Market(s)

Potential bankruptcy clients.

Industry/Entity Type

Legal

Colors

Designer to choose colors to be used in the design.

Requirements
Must have
• Address for locations, phone number, and website address.
• Addresses are on website larkmoorfirm.legal. Use following phone number (for tracking purposes): 404-731-2864

```html
<!DOCTYPE html>
<html lang="en">
<head>
<meta charset="utf-8">
<title>Larkmoor Firm Letterhead</title>
<link href="https://fonts.googleapis.com/css2?family=Lato:wght@300;400&family=Roboto:wght@400;500&display=swap" rel="stylesheet">
<style>
  :root {
    --backdrop: #e9e7e3;
    --paper: #ffffff;
    --charcoal: #3d3d3d;
    --sage: #80bd86;
    --ink: #3a3a3a;
    --ink-soft: #555555;
    --on-sage: #ffffff;
  }
  * { margin: 0; padding: 0; box-sizing: border-box; }
  html, body {
    width: 1200px; height: 1120px; overflow: hidden;
    background: var(--backdrop);
  }
  .letterhead {
    position: absolute; left: 191px; top: 20px;
    width: 818px; height: 1080px;
    background: var(--paper);
    box-shadow: 0 4px 14px rgba(0,0,0,0.18);
    overflow: hidden;
    font-family: "Lato", sans-serif;
    color: var(--ink);
  }
  .header-shapes { position: absolute; left: 0; top: 0; }
  .contact {
    position: absolute; left: 587px; top: 33px;
    font-family: "Roboto", sans-serif; font-size: 12px; line-height: 15px;
    color: var(--on-sage); letter-spacing: -0.1px;
  }
  .contact .address { margin-bottom: 9px; font-weight: 500; }
  .contact .line { display: flex; align-items: center; gap: 6px; height: 16px; }
  .contact svg { width: 10px; height: 10px; flex: none; }
  .brand {
    position: absolute; left: 68px; top: 88px;
    display: flex; align-items: center; gap: 12px;
  }
  .brand-mark { width: 30px; height: 30px; border-radius: 50%; background: var(--sage); }
  .brand-name {
    font-family: "Lato", sans-serif; font-weight: 400; font-size: 30px;
    color: var(--sage); letter-spacing: 0.2px;
  }
  .date { position: absolute; left: 69px; top: 245px; font-size: 16px; }
  .recipient { position: absolute; left: 69px; top: 290px; font-size: 15.5px; line-height: 19px; }
  .recipient .name { font-weight: 400; font-size: 16px; }
  .recipient .addr { font-weight: 300; }
  .body-copy {
    position: absolute; left: 69px; top: 413px; width: 671px;
    font-size: 15px; line-height: 23px; font-weight: 300;
    text-align: justify; hyphens: auto;
  }
  .body-copy p + p { margin-top: 22px; }
  .signature { position: absolute; left: 69px; top: 848px; }
  .signature .signer { font-size: 20px; font-weight: 400; }
  .signature .role { font-size: 14px; font-weight: 300; color: var(--ink-soft); margin-top: 6px; }
  .footer-band {
    position: absolute; left: 0; bottom: 0; width: 818px; height: 19px;
    background: var(--sage);
  }
</style>
</head>
<body>
<main class="letterhead">
  <svg class="header-shapes" width="818" height="140" viewBox="0 0 818 140" aria-hidden="true">
    <polygon points="0,0 458,0 495,55 0,55" fill="var(--charcoal)"/>
    <path d="M458 0 H818 V132 H592 Q566 132 552 113 Z" fill="var(--sage)"/>
  </svg>

  <div class="contact">
    <div class="address">Address, demo street 088<br>P.O. Box 000, 555 Avenue</div>
    <div class="line">
      <svg viewBox="0 0 10 10"><path d="M2 0.8 L3.6 2.6 L2.8 3.8 Q3.9 6 6.2 7.2 L7.4 6.4 L9.2 8 L8 9.4 Q3.5 9 0.6 2 Z" fill="#fff"/></svg>
      404-731-2864
    </div>
    <div class="line">
      <svg viewBox="0 0 10 10"><rect x="0.5" y="2" width="9" height="6" fill="#fff"/><path d="M0.5 2 L5 5.5 L9.5 2" fill="none" stroke="var(--sage)" stroke-width="0.9"/></svg>
      info@websitename.com
    </div>
    <div class="line">
      <svg viewBox="0 0 10 10"><circle cx="5" cy="5" r="4.3" fill="none" stroke="#fff" stroke-width="0.9"/><ellipse cx="5" cy="5" rx="1.8" ry="4.3" fill="none" stroke="#fff" stroke-width="0.8"/><line x1="0.7" y1="5" x2="9.3" y2="5" stroke="#fff" stroke-width="0.8"/></svg>
      www.websitename.com
    </div>
  </div>

  <div class="brand">
    <span class="brand-mark"></span>
    <span class="brand-name">Larkmoor Firm</span>
  </div>

  <p class="date">May 10, 2018</p>

  <div class="recipient">
    <p class="name">Dear Mr. Penrow</p>
    <p class="addr">demo street,<br>demo placeP.O.<br>Box 000, 555 Avenue</p>
  </div>

  <div class="body-copy">
    <p>Lorem ipsum dolor sit amet, consectetur adipiscing elit. Donec orci purus, luctus vitae dignissim eu, iaculis sed purus. Vivamus faucibus, ipsum nec aliquet viverra, leo mauris condimentum ligula, sit amet sagittis enim ligula quis arcu. Nam egestas tortor id nisi porttitor mattis. In tortor ante, ultricies in suscipit a, tempus non massa. Vivamus et auctor mi. Fusce vel massa nulla. Phasellus nec eros mauris, et scelerisque orci. Donec malesuada orci vitae nulla accumsan porta a id massa. Quisque accumsan iaculis magna sit amet fringilla. Maecenas consequat, magna eget tincidunt semper, odio nibh rutrum mi, id feugiat ante nisi eu risus. Vestibulum nunc orci, rhoncus a placerat in, ultricies in mi. Cras mattis varius eros, vel fringilla nisi suscipit eget.</p>
    <p>Quisque scelerisque sagittis nulla at porttitor. Mauris a justo et tellus interdum tristique. Sed id augue vitae urna euismod commodo aliquet a quam. Pellentesque arcu velit, cursus et malesuada ut, consequat et diam. Nullam erat sem, rhoncus id ullamcorper vitae, rhoncus et arcu. In ultricies ultricies nulla, ut rutrum nisi iaculis at. Donec eu magna a metus ornare faucibus. Fusce aliquet faucibus ultricies. Morbi semper, est id tincidunt gravida, sem arcu adipiscing lacus, ac bibendum nulla leo eu purus. Quisque nec diam sed risus consectetur a ccumsan quis quis nibh. Vestibulum id purus lorem.</p>
  </div>

  <div class="signature">
    <p class="signer">John Doe</p>
    <p class="role">Co-Founder &amp; CEO</p>
  </div>

  <div class="footer-band"></div>
</main>
</body>
</html>
```